bluegum ridge coaching needs snazzy business card that serves a dual purpose

business card needed for a Bluegum Ridge Coaching company that takes people out on the road to teach them proficiency on their bike.
My business logo is attached. I have grey and aqua colours with my logo.
i really like bitumen/tarmac/ road in the design somehow but that is up to you.
I think navy blue will go well with my colours too. see how you go.

I want this card to look REALLY good.
the back of the card may be used for emergency contact details too
In case of Emergency I am:
Name:

Emergency Contact name
emergency contact Phone number:

• details that are essential are:
• logo
• Name: Helena FORD
• ABN: 53 291 804 667
• phone number: 0455 128 906
• chatterly logo
• * ride tuition & proficiency
• * skills practice
• * maintenance 101
• * bike fitting service
• * cater for all ages & abilities
• backpage:
• logo
• skills confidence enjoyment
• some space for writing
• nothing girly. The business will already naturally attract women, it needs to appeal to both genders

```html
<!DOCTYPE html>
<html lang="en">
<head>
<meta charset="utf-8">
<title>Bluegum Ridge Coaching – Business Card</title>
<link href="https://fonts.googleapis.com/css2?family=Open+Sans:wght@400;600;700&display=swap" rel="stylesheet">
<style>
  :root {
    --backdrop: #e4e5e7;
    --asphalt-light: #6a6b6e;
    --asphalt-dark: #4c4d50;
    --aqua: #3fc0ae;
    --lane-white: #f2f2f2;
    --ink-white: #ffffff;
  }
  * { box-sizing: border-box; margin: 0; padding: 0; }
  html, body {
    width: 1200px; height: 1000px; overflow: hidden;
    background: var(--backdrop);
    font-family: "Open Sans", Arial, sans-serif;
  }
  .sheet { position: relative; width: 1200px; height: 1000px; }
  .card {
    position: absolute; left: 240px; width: 720px; height: 411px;
    background: linear-gradient(160deg, var(--asphalt-light), var(--asphalt-dark));
    border-radius: 4px;
    box-shadow: 0 10px 28px rgba(0,0,0,.25);
    overflow: hidden;
  }
  .card--back { top: 60px; }
  .card--front { top: 529px; }
  .brand {
    position: absolute; display: flex; align-items: center; gap: 14px;
    color: var(--aqua); font-weight: 600; font-size: 40px; letter-spacing: .5px;
  }
  .brand__dot { width: 22px; height: 22px; border-radius: 50%; background: var(--aqua); }
  .card--back .brand { left: 120px; top: 82px; }
  .card--front .brand { left: 170px; top: 52px; }
  .lane-markings {
    position: absolute; left: 0; right: 0; display: flex; justify-content: space-between;
    padding: 0 30px;
  }
  .lane-markings span { width: 104px; height: 22px; background: var(--lane-white); }
  .card--back .lane-markings { top: 180px; }
  .card--front .lane-markings { top: 165px; }
  .tagline {
    position: absolute; left: 0; right: 0; top: 226px; text-align: center;
    color: var(--aqua); font-weight: 700; font-size: 31px;
  }
  .contact { position: absolute; left: 50px; top: 222px; color: var(--ink-white); }
  .contact__name { font-weight: 700; font-size: 26px; margin-bottom: 14px; }
  .contact__line { font-size: 20px; line-height: 30px; }
  .social {
    position: absolute; left: 50px; top: 350px; display: flex; align-items: center; gap: 10px;
    color: var(--ink-white); font-size: 18px; font-weight: 400;
  }
  .social__square { width: 24px; height: 24px; background: var(--ink-white); border-radius: 3px; opacity: .85; }
  .services {
    position: absolute; left: 410px; top: 214px; list-style: none;
    color: var(--ink-white); font-size: 19px; line-height: 29px;
  }
  .services li::before { content: "*"; color: var(--aqua); font-weight: 700; font-size: 24px; margin-right: 12px; }
</style>
</head>
<body>
<main class="sheet">
  <section class="card card--back" aria-label="Card back">
    <div class="brand"><span class="brand__dot"></span>Bluegum Ridge Coaching</div>
    <div class="lane-markings"><span></span><span></span><span></span><span></span><span></span></div>
    <p class="tagline">skills confidence enjoyment</p>
  </section>

  <section class="card card--front" aria-label="Card front">
    <div class="brand"><span class="brand__dot"></span>Bluegum Ridge Coaching</div>
    <div class="lane-markings"><span></span><span></span><span></span><span></span><span></span></div>
    <div class="contact">
      <p class="contact__name">Helena FORD</p>
      <p class="contact__line">ABN: 53 291 804 667</p>
      <p class="contact__line">phone: 0455 128 906</p>
    </div>
    <div class="social"><span class="social__square"></span>chatterly</div>
    <ul class="services">
      <li>ride tuition &amp; proficiency</li>
      <li>skills practice</li>
      <li>maintenance 101</li>
      <li>bike fitting service</li>
      <li>center for all ages &amp; abilities</li>
    </ul>
  </section>
</main>
</body>
</html>
```